Looking for an Innovative Print Design (Service Directory)

We need a new design for our advertisement within a printed colour services directory.

We are a compensation law firm called Velbrook Compensation Lawyers. Feel free to take a browse of our website www.velbrooklegal.com.au to get an idea of what we do and the kind of firm we are.

We are in the process of redeveloping our website and as such, so please don't adhere to the design principles of the current site- impress us with your originality!

On top of any editable formats, your final submissions must include a .pdf copy.
The same design will need to be presented in two dimensions:

- 154mm x 118mm (B1/B2 Half Page);
- 175mm x 113mm (B4 Half Page).

[For more information refer to attached Pdf.]

We have attached for you a few examples of other firms' designs (Sample1,2,3). These are by no means good, or what we're after, it's just to provide you with an idea of what sort of advertisements go into the service directory.

Hi all,

We want to emphasise that a priority of the design is that it must look:
• Professional
• Sophisticated
Please do not hesitate to use completely different colour schemes to the ones that are on our website- as we have said, our website will change in the near future, so cohesion between the current project and the website is not necessary!

Thanks!

Thank you for your submissions so far. There are some great ideas hidden in there. 

An issue we are having is that most of you are conforming to the same understanding of what it should look like. Remember that there is NO NEED to be bound by the image of firm as is. That is, feel free to use a different colour logo.

For inspiration, we relate well to the design aesthetics of: http://www.tinfernstudio.co.uk/

Look forward to seeing your 'out of the box' submissions. 

Reason: We've received a large amount of fantastic designs. However, what we're really looking for is something original. Please feel free to think outside the box (the final design doesn't need to look like a print ad), and construct a design that is completely incongruous with our website! While we do appreciate a minimalistic design, we have yet to receive something that really grabs your attention with its visuals. We're not sure but this may or may not be achieved with a full colour design. Thanks for all your submissions- they all have some features that really click with us. We look forward to the next wave of submissions!

Target Market(s)

We have various target markets, including mainly families, elderly people, blue collar workers.

These are individuals who are looking for assistance. They feel helpless or wronged.

Keep in mind that the people accessing these are those who prefer going to a printed directory rather than using a google search.

Industry/Entity Type

Law Firm

Font styles to use
Serif
Sans Serif

Requirements
Must have
• - Our name 'Velbrook Compensation Lawyers'
- Our logo (attached as logo.eps, logo.png, and logo.tif)
- Must include phone number as 1300 XXX XXX (this must be prominent)
- Must include the following service areas in these words: Motor vehicle claims, medical claims, superannuation claims, Workplace claims, negligence claims
- Our email address: info@velbrooklegal.com.au
- Our website address: www.velbrooklegal.com.au
- The following catchphrases: '98% success rate', and 'No win no fee' in those words
- Our location '412 Carvel Lane, Smithville, SYDNEY'
- For sizing dimensions, we need one in 154mm x 118mm and also a design in 175mm x 113mm (B4 Half Page) [refer to pdf attached]
Nice to have
• - Text indicating free initial consulatation
- Professional colour scheme
- As our website will be changed, do not worry about making the advertisement cohesive with our website design
- We want the design to be modern, but still professional
- Clean typeface
- No gradient colour scheme
- When designing, if you are looking to place more text onto the advertisement, these may be some considerations (feel free to change the wording): Accredited specialists, home and hospital visits

```html
<!DOCTYPE html>
<html lang="en">
<head>
<meta charset="utf-8">
<title>Velbrook Compensation Lawyers – Directory Advertisement</title>
<link rel="stylesheet" href="https://fonts.googleapis.com/css2?family=Montserrat:wght@400;600&family=Raleway:wght@400;500&family=Exo+2:wght@600&family=Arimo:wght@700&display=swap">
<style>
  :root {
    --brand-blue: #357693;
    --brand-orange: #ef7222;
    --ink-grey: #3d4549;
    --fold-grey: #2c3336;
    --paper: #ffffff;
    --backdrop: #e9e9e7;
  }
  * { margin: 0; padding: 0; box-sizing: border-box; }
  html, body {
    width: 1200px; height: 814px; overflow: hidden;
    background: var(--backdrop);
  }
  .stage { position: relative; width: 1200px; height: 814px; }
  .ad {
    position: absolute; left: 40px; top: 44px;
    width: 1032px; height: 668px;
    background: var(--paper);
    transform: scale(1.0853); transform-origin: 0 0;
    overflow: hidden;
  }
  .ad-shapes { position: absolute; inset: 0; width: 1032px; height: 668px; }

  .brand { position: absolute; left: 153px; top: 52px; display: flex; align-items: center; }
  .brand-dot {
    width: 166px; height: 166px; border-radius: 50%;
    background: var(--brand-orange); flex: none;
  }
  .brand-name {
    margin-left: 42px;
    font-family: "Montserrat", sans-serif; font-weight: 400;
    color: var(--ink-grey); line-height: 1;
  }
  .brand-name .firm { display: block; font-size: 88px; letter-spacing: 5px; }
  .brand-name .practice { display: block; font-size: 27px; letter-spacing: 5.5px; margin-top: 12px; }

  .services {
    position: absolute; left: 56px; top: 286px; list-style: none;
    font-family: "Raleway", sans-serif; font-weight: 400;
    font-size: 32px; color: var(--paper);
  }
  .services li { height: 58.5px; display: flex; align-items: center; }
  .services li::before {
    content: ""; width: 11px; height: 11px; border-radius: 50%;
    border: 4px solid var(--brand-orange); margin-right: 11px; flex: none;
  }

  .tagline {
    position: absolute; left: 34px; top: 600px;
    font-family: "Arimo", sans-serif; font-weight: 700;
    font-size: 28px; color: var(--paper); letter-spacing: 0.3px;
  }

  .offer {
    position: absolute; left: 553px; top: 240px; width: 426px; height: 145px;
    display: flex; flex-direction: column; justify-content: center; align-items: center;
    font-family: "Exo 2", sans-serif; font-weight: 600;
    font-size: 42px; line-height: 1.3; color: var(--paper); text-align: center;
  }

  .contact {
    position: absolute; left: 553px; top: 418px; width: 426px; text-align: center;
    color: var(--paper);
  }
  .call { font-family: "Arimo", sans-serif; font-weight: 700; font-size: 40px; line-height: 54px; }
  .details {
    list-style: none; margin-top: 20px;
    font-family: "Raleway", sans-serif; font-weight: 400; font-size: 19.5px; line-height: 31px;
  }
  .details li { display: flex; justify-content: center; align-items: center; gap: 6px; }
  .details svg { width: 16px; height: 16px; flex: none; }
</style>
</head>
<body>
<div class="stage">
  <div class="ad">
    <svg class="ad-shapes" viewBox="0 0 1032 668" aria-hidden="true">
      <path d="M370,0 L1032,0 L1032,30 L420,30 C395,30 392,0 370,0 Z" fill="var(--brand-blue)"/>
      <path d="M0,198 L95,198 C140,198 148,255 205,255 L1032,255 L1032,668 L0,668 Z" fill="var(--brand-blue)"/>
      <rect x="0" y="640" width="1032" height="28" fill="var(--brand-orange)"/>
      <path d="M0,582 L470,582 C512,582 518,640 565,640 L565,668 L0,668 Z" fill="var(--brand-orange)"/>
      <path d="M527,255 L553,240 L553,255 Z" fill="var(--fold-grey)"/>
      <path d="M1005,255 L979,240 L979,255 Z" fill="var(--fold-grey)"/>
      <path d="M553,240 L979,240 L979,373 Q979,385 967,385 L565,385 Q553,385 553,373 Z" fill="var(--brand-orange)"/>
    </svg>

    <div class="brand">
      <div class="brand-dot"></div>
      <h1 class="brand-name"><span class="firm">VELBROOK</span><span class="practice">COMPENSATION LAWYERS</span></h1>
    </div>

    <ul class="services">
      <li>Motor Vehicle Claims</li>
      <li>Medical Claims</li>
      <li>Superannuation Claims</li>
      <li>Workplace Claims</li>
      <li>Negligence Claims</li>
    </ul>

    <p class="tagline">REAL PEOPLE, REAL RESULTS</p>

    <p class="offer"><span>98% Success Rate</span><span>&amp; No Win No Fee</span></p>

    <div class="contact">
      <p class="call">Call us now :<br>1300 XXX XXX</p>
      <ul class="details">
        <li><svg viewBox="0 0 16 16"><path d="M8 1a5 5 0 0 0-5 5c0 4 5 9 5 9s5-5 5-9a5 5 0 0 0-5-5zm0 7a2 2 0 1 1 0-4 2 2 0 0 1 0 4z" fill="#fff"/></svg>412 Carvel Lane, Smithville, SYDNEY</li>
        <li><svg viewBox="0 0 16 16"><rect x="1" y="3" width="14" height="10" fill="none" stroke="#fff" stroke-width="1.5"/><path d="M1 3l7 6 7-6" fill="none" stroke="#fff" stroke-width="1.5"/></svg>name@velbrooklegal.com.au</li>
        <li><svg viewBox="0 0 16 16"><circle cx="8" cy="8" r="6.5" fill="none" stroke="#fff" stroke-width="1.4"/><ellipse cx="8" cy="8" rx="2.8" ry="6.5" fill="none" stroke="#fff" stroke-width="1.2"/><path d="M1.5 8h13M2.5 5h11M2.5 11h11" stroke="#fff" stroke-width="1.1"/></svg>www.velbrooklegal.com.au</li>
      </ul>
    </div>
  </div>
</div>
</body>
</html>
```